Wolkenfeld - a property developer - Website design

Hi all!
Exciting new project for you! :)
We are looking for some creative/modern designs to best represent us as a company.
Please have a look at the following link: huhu.wolkenfeld.eu to get an idea about who we are and what we do.
The 'Main Page' of the HP should be neatly arranged, easy to navigate, contain several pictures (changing every 10 seconds or so) that should reflect that we are property developers.
The navigation points ('About us', 'Projects' 'Investment', 'Contact Us', 'Legal Notice') should be included in the Design (again under every navigation point, pictures may be added - that reflect our profession and/or the subsection)
What we will need at the end of the day is a fully functional site - i.e: a site that is designed and programmed with backend/wordpress, to allow us to make changes anytime we feel like it.
Further questions?! Don't hesitate to contact me! Thanks :)
Target Market(s)
Real Estate Development/Building sector
Industry/Entity Type
Real Estate Development
Number of Pages Required
5+ page
Look and feel

```html
<!DOCTYPE html>
<html lang="en">
<head>
<meta charset="utf-8">
<title>Wolkenfeld – Property Development</title>
<link rel="stylesheet" href="https://fonts.googleapis.com/css2?family=Montserrat:wght@400;600;700&family=Nunito+Sans:wght@400;600&display=swap">
<style>
  :root {
    --ink: #3a3a3a;
    --ink-soft: #555;
    --muted: #8d8d8d;
    --rule: #e3e3e3;
    --paper: #ffffff;
    --sky-top: #5b9ad6;
    --sky-low: #a9cdea;
    --tree: #5f7350;
  }
  * { box-sizing: border-box; margin: 0; padding: 0; }
  html, body { width: 1036px; height: 1200px; overflow: hidden; background: var(--paper); }
  body { position: relative; font-family: "Nunito Sans", sans-serif; color: var(--ink); }

  .site-header { position: absolute; top: 0; left: 0; width: 1036px; height: 54px; }
  .brand { position: absolute; left: 27px; top: 22px; font-family: "Montserrat", sans-serif; font-size: 11.5px; letter-spacing: 0.6px; color: var(--ink); }
  .main-nav a { position: absolute; top: 24px; font-family: "Montserrat", sans-serif; font-size: 8.8px; letter-spacing: 0.5px; color: var(--ink-soft); text-decoration: none; }

  .hero { position: absolute; top: 54px; left: 0; width: 1036px; height: 415px;
    background: linear-gradient(180deg, var(--sky-top) 0%, var(--sky-low) 55%, #8fa3b3 75%, var(--tree) 100%); }
  .hero-dots { position: absolute; top: 394px; left: 496px; display: flex; gap: 6px; }
  .hero-dots span { width: 10px; height: 10px; border-radius: 50%; border: 1.2px solid #fff; }
  .hero-dots span.is-active { background: #fff; }
  .lang-switch { position: absolute; top: 108px; left: 0; width: 27px; height: 27px; background: #fff;
    font-family: "Montserrat", sans-serif; font-size: 8.5px; font-weight: 600; text-align: center; padding-top: 5px; color: var(--ink); }
  .lang-switch svg { display: block; margin: 1px auto 0; }

  .section-title { position: absolute; left: 0; width: 1036px; text-align: center;
    font-family: "Montserrat", sans-serif; font-weight: 700; font-size: 16.5px; letter-spacing: 2.2px; color: var(--ink); }
  .section-title::after { content: ""; display: block; width: 66px; height: 1px; background: var(--rule); margin: 5px auto 0; }

  .history-text { position: absolute; top: 574px; left: 293px; width: 450px; text-align: center;
    font-size: 12.2px; line-height: 17.3px; color: var(--muted); }
  .btn-more { position: absolute; top: 670px; left: 451px; width: 135px; height: 35px; border: 1.5px solid var(--ink);
    font-family: "Montserrat", sans-serif; font-size: 9px; font-weight: 600; letter-spacing: 1.2px;
    display: flex; align-items: center; justify-content: center; color: var(--ink); text-decoration: none; }

  .project-list { position: absolute; top: 872px; left: 248px; display: flex; gap: 6px; }
  .project-card { width: 130px; text-align: center; }
  .project-photo { height: 97px; }
  .project-name { margin-top: 7px; font-family: "Montserrat", sans-serif; font-weight: 700; font-size: 8px; letter-spacing: 1.3px; color: var(--ink); }
  .project-note { margin-top: 3px; font-size: 6.8px; color: var(--muted); }

  .site-footer { position: absolute; top: 1052px; left: 0; width: 1036px; border-top: 1px solid var(--rule); text-align: center; }
  .legal-link { display: inline-block; margin-top: 23px; font-family: "Montserrat", sans-serif; font-weight: 600; font-size: 7.5px; letter-spacing: 0.8px; color: var(--ink); }
  .copyright { margin-top: 16px; font-family: "Montserrat", sans-serif; font-size: 7px; letter-spacing: 0.5px; color: var(--ink); }
</style>
</head>
<body>
  <header class="site-header">
    <div class="brand">WOLKENFELD</div>
    <nav class="main-nav">
      <a href="#" style="left:732px">ABOUT</a>
      <a href="#" style="left:790px">PROJECTS</a>
      <a href="#" style="left:868px">INVESTMENTS</a>
      <a href="#" style="left:965px">CONTACT</a>
    </nav>
  </header>

  <section class="hero" role="img" aria-label="Modern glass residential tower under a blue sky with trees and neighbouring buildings">
    <div class="hero-dots"><span class="is-active"></span><span></span><span></span></div>
  </section>
  <div class="lang-switch">EN
    <svg width="8" height="4" viewBox="0 0 8 4"><path d="M0 0 L4 4 L8 0" fill="none" stroke="#999" stroke-width="0.8"/></svg>
  </div>

  <h2 class="section-title" style="top:520px">OUR HISTORY</h2>
  <p class="history-text">Wolkenfeld is a combination of potent companies pursuing a common goal: the realization of modern, sustainable housing projects for highest demands in Vienna. Our building companies' efforts are concentrating on the two core areas of new developments and roof extensions...</p>
  <a class="btn-more" href="#">READ MORE</a>

  <h2 class="section-title" style="top:808px">PROJECTS</h2>
  <div class="project-list">
    <article class="project-card">
      <div class="project-photo" role="img" aria-label="Row of terraced houses with lawn" style="background:linear-gradient(180deg,#6aa0dc 0%,#d8d0c0 45%,#c9bfa9 75%,#7d9a4e 100%)"></div>
      <div class="project-name">LINDENHAINWEG</div>
      <div class="project-note">Lorem ipsum dolor sit amet.</div>
    </article>
    <article class="project-card">
      <div class="project-photo" role="img" aria-label="White modern house with balconies" style="background:linear-gradient(180deg,#5d92d4 0%,#e6ecf2 40%,#f2f4f6 80%,#9aa09a 100%)"></div>
      <div class="project-name">MOHRGASSE</div>
      <div class="project-note">Lorem ipsum dolor sit amet.</div>
    </article>
    <article class="project-card">
      <div class="project-photo" role="img" aria-label="Beige period apartment building facade" style="background:linear-gradient(180deg,#9fb3c8 0%,#d6c8ad 40%,#cbbb9c 100%)"></div>
      <div class="project-name">ULMENBACHGASSE</div>
      <div class="project-note">Lorem ipsum dolor sit amet.</div>
    </article>
    <article class="project-card">
      <div class="project-photo" role="img" aria-label="Historic townhouses behind trees" style="background:linear-gradient(180deg,#4a4a40 0%,#a08a78 45%,#8c6f5b 80%,#3f3a33 100%)"></div>
      <div class="project-name">FERNGASSE</div>
      <div class="project-note">Lorem ipsum dolor sit amet.</div>
    </article>
  </div>

  <footer class="site-footer">
    <a class="legal-link" href="#">LEGAL NOTICE</a>
    <div class="copyright">(C) COPYRIGHT WOLKENFELD 2015</div>
  </footer>
</body>
</html>
```